Coffee to go business card

Can you make an Orange card please.
our other colours are black chocolate and white for the writing.
If you could make the name and phone number more prominant.

Target Market(s)

People on the go.

Industry/Entity Type

Business

Contact Information for Business Card

Vireo Espresso Bar - coffee to go
Open at the Orange window
Weekdays 5.30am to 2.30pm
Saturdays 7.30am to 2.00pm
Phone orders welcome 58361907
Shop 9 Brindle Court Centre
17 Tallow Street, Brindle COurt, 4937
Serving Fresh Quarzo Espresso
Like us on Friendline

Requirements
Must have
• I have attached our logo but not dure if it uploaded correctly?
Nice to have
• see above

```html
<!DOCTYPE html>
<html lang="en">
<head>
<meta charset="utf-8">
<title>Vireo Espresso Bar – Business Card</title>
<link rel="stylesheet" href="https://fonts.googleapis.com/css2?family=Alegreya:ital,wght@1,400;1,500&display=swap">
<style>
  :root {
    --bg-peach: #fdb47c;
    --bg-yellow: #fefb7a;
    --bg-warm: #fdc27d;
    --card-orange: #f38d1f;
    --ink-brown: #4b2514;
    --bean-dark: #3e1f12;
    --bean-mid: #7a4127;
    --bean-light: #a0613a;
    --divider: #5a2c17;
    --cup-tone: #d7762a;
    --shadow: rgba(40, 25, 10, 0.55);
  }
  * { margin: 0; padding: 0; box-sizing: border-box; }
  html, body { width: 1200px; height: 1000px; overflow: hidden; }
  body {
    position: relative;
    background: linear-gradient(135deg, var(--bg-peach) 0%, var(--bg-yellow) 45%, var(--bg-yellow) 60%, var(--bg-warm) 100%);
    font-family: "Alegreya", "Palatino Linotype", serif;
    font-style: italic;
    color: var(--ink-brown);
  }
  .card {
    position: absolute;
    width: 776px;
    height: 430px;
    background: var(--card-orange);
    border-radius: 18px;
    overflow: hidden;
    box-shadow: 9px 11px 10px var(--shadow);
  }
  .card--front { left: 35px; top: 38px; }
  .card--back { left: 380px; top: 525px; }
  .bean-panel {
    position: absolute;
    left: 0; top: 0;
    width: 266px; height: 100%;
    border-right: 2px solid var(--divider);
    background:
      radial-gradient(circle at 30% 25%, var(--bean-light) 0%, transparent 35%),
      radial-gradient(circle at 70% 60%, var(--bean-light) 0%, transparent 30%),
      radial-gradient(circle at 40% 85%, var(--bean-mid) 0%, transparent 40%),
      linear-gradient(90deg, var(--bean-dark) 0%, var(--bean-mid) 20%, var(--bean-mid) 80%, var(--bean-dark) 100%);
  }
  .card--back .bean-panel { width: 268px; }
  .text { position: absolute; white-space: nowrap; line-height: 1; }
  .brand-name {
    left: 270px; width: 476px; top: 28px;
    text-align: center; font-size: 49px; font-weight: 400;
  }
  .brand-rule {
    position: absolute; left: 270px; top: 82px;
    width: 470px; height: 2px; background: var(--ink-brown);
  }
  .tagline { left: 270px; width: 476px; top: 108px; text-align: center; font-size: 36px; }
  .hours-label { left: 340px; font-size: 30px; }
  .hours-time { right: 33px; font-size: 30px; }
  .window-note { left: 270px; width: 484px; top: 373px; text-align: center; font-size: 30px; }
  .cup { position: absolute; }
  .phone-line { left: 306px; top: 30px; font-size: 38px; }
  .phone-number { border-bottom: 2px solid var(--ink-brown); padding-right: 8px; }
  .info-line { font-size: 30px; }
</style>
</head>
<body>

<section class="card card--front" aria-label="Business card front">
  <div class="bean-panel" role="img" aria-label="Photograph of roasted coffee beans"></div>

  <h1 class="text brand-name">Vireo Espresso Bar</h1>
  <div class="brand-rule"></div>
  <p class="text tagline">- coffee to go -</p>

  <svg class="cup" style="left:283px;top:196px" width="52" height="54" viewBox="0 0 52 54" aria-hidden="true">
    <path d="M18 4 q-5 6 0 12 q5 6 0 12 M26 2 q-5 6 0 12 q5 6 0 12" fill="none" stroke="var(--cup-tone)" stroke-width="2"/>
    <path d="M6 28 h34 v6 q0 14 -17 14 q-17 0 -17 -14 z" fill="var(--cup-tone)"/>
    <path d="M40 32 q9 0 8 6 q-1 6 -10 6" fill="none" stroke="var(--cup-tone)" stroke-width="3"/>
    <ellipse cx="24" cy="50" rx="22" ry="3" fill="var(--cup-tone)"/>
  </svg>
  <p class="text hours-label" style="top:206px">Weekdays :</p>
  <p class="text hours-time" style="top:240px">5.30am to 2.30pm</p>

  <svg class="cup" style="left:283px;top:254px" width="52" height="54" viewBox="0 0 52 54" aria-hidden="true">
    <path d="M18 4 q-5 6 0 12 q5 6 0 12 M26 2 q-5 6 0 12 q5 6 0 12" fill="none" stroke="var(--cup-tone)" stroke-width="2"/>
    <path d="M6 28 h34 v6 q0 14 -17 14 q-17 0 -17 -14 z" fill="var(--cup-tone)"/>
    <path d="M40 32 q9 0 8 6 q-1 6 -10 6" fill="none" stroke="var(--cup-tone)" stroke-width="3"/>
    <ellipse cx="24" cy="50" rx="22" ry="3" fill="var(--cup-tone)"/>
  </svg>
  <p class="text hours-label" style="top:274px">Saturdays :</p>
  <p class="text hours-time" style="top:305px">7.30am to 2.00pm</p>

  <p class="text window-note">~Open at the Orange window~</p>
</section>

<section class="card card--back" aria-label="Business card back">
  <div class="bean-panel" role="img" aria-label="Photograph of roasted coffee beans"></div>

  <svg class="cup" style="left:272px;top:36px" width="30" height="30" viewBox="0 0 52 54" aria-hidden="true">
    <path d="M18 4 q-5 6 0 12 q5 6 0 12 M26 2 q-5 6 0 12 q5 6 0 12" fill="none" stroke="var(--cup-tone)" stroke-width="3"/>
    <path d="M6 28 h34 v6 q0 14 -17 14 q-17 0 -17 -14 z" fill="var(--cup-tone)"/>
    <path d="M40 32 q9 0 8 6 q-1 6 -10 6" fill="none" stroke="var(--cup-tone)" stroke-width="4"/>
  </svg>
  <p class="text phone-line">Phone orders :<span class="phone-number">58361907</span></p>

  <svg class="cup" style="left:272px;top:170px" width="30" height="30" viewBox="0 0 52 54" aria-hidden="true">
    <path d="M18 4 q-5 6 0 12 q5 6 0 12 M26 2 q-5 6 0 12 q5 6 0 12" fill="none" stroke="var(--cup-tone)" stroke-width="3"/>
    <path d="M6 28 h34 v6 q0 14 -17 14 q-17 0 -17 -14 z" fill="var(--cup-tone)"/>
    <path d="M40 32 q9 0 8 6 q-1 6 -10 6" fill="none" stroke="var(--cup-tone)" stroke-width="4"/>
  </svg>
  <p class="text info-line" style="left:306px;top:170px">Shop 9 : Brindle Court Centre</p>
  <p class="text info-line" style="left:452px;top:203px">17 Tallow Street,</p>
  <p class="text info-line" style="left:484px;top:236px">Brindle COurt, 4937</p>

  <svg class="cup" style="left:272px;top:302px" width="30" height="30" viewBox="0 0 52 54" aria-hidden="true">
    <path d="M18 4 q-5 6 0 12 q5 6 0 12 M26 2 q-5 6 0 12 q5 6 0 12" fill="none" stroke="var(--cup-tone)" stroke-width="3"/>
    <path d="M6 28 h34 v6 q0 14 -17 14 q-17 0 -17 -14 z" fill="var(--cup-tone)"/>
    <path d="M40 32 q9 0 8 6 q-1 6 -10 6" fill="none" stroke="var(--cup-tone)" stroke-width="4"/>
  </svg>
  <p class="text info-line" style="left:306px;top:302px">Serving Fresh Quarzo Espresso!</p>

  <svg class="cup" style="left:272px;top:368px" width="30" height="30" viewBox="0 0 52 54" aria-hidden="true">
    <path d="M18 4 q-5 6 0 12 q5 6 0 12 M26 2 q-5 6 0 12 q5 6 0 12" fill="none" stroke="var(--cup-tone)" stroke-width="3"/>
    <path d="M6 28 h34 v6 q0 14 -17 14 q-17 0 -17 -14 z" fill="var(--cup-tone)"/>
    <path d="M40 32 q9 0 8 6 q-1 6 -10 6" fill="none" stroke="var(--cup-tone)" stroke-width="4"/>
  </svg>
  <p class="text info-line" style="left:306px;top:368px">Like us on Friendline!</p>
</section>

</body>
</html>
```